Pure Palm tree rhum label design

We need a label design for a palm tree rhum named 'Voile Cendré'. We have an original design and we need an enhancement or a new design that reflects the product. It is a liquor. The label should be bilingual (French and English). We have original design that gives an idea and can be used as starting point. The text on the label for the existing design has to show up in the new design. The text is uploaded too as well as the existing design.
Update:
- The design must use Oil Palm Tree and not Palm Tree. Sample Images are attached.
- The neck of the bottle has to have the name of the product: Voile Cendré.
- The word 'Liqueur' goes between the volume (1L) and the percentage of alcohol (43% Vol).
- Back side text is provided: see document
- The following description goes between the English and the french version (front and back):
The word: L'Original
The representation of a palm oil tree
The word: Original.
An image is uploaded for that.
No mandatory Fonts or Color or Bakground.

Font styles to use
Serif
Sans Serif
Script

```html
<!DOCTYPE html>
<html lang="fr">
<head>
<meta charset="utf-8">
<title>Voile Cendré – Sodabi rectifié</title>
<link rel="stylesheet" href="https://fonts.googleapis.com/css2?family=Almendra+SC&family=Yellowtail&family=La+Belle+Aurore&family=Courier+Prime&family=Libre+Baskerville&display=swap">
<style>
  :root {
    --page: #f4f4f2;
    --paper: #e7e0c7;
    --ink: #353535;
    --ink-soft: #5a5750;
    --ink-faint: #8a857a;
    --band: #2b2b2b;
    --neck-text: #e4dcc0;
    --palm: #8a8676;
  }
  * { box-sizing: border-box; margin: 0; padding: 0; }
  html, body { width: 1062px; height: 1200px; overflow: hidden; background: var(--page); }
  .canvas { position: relative; width: 1062px; height: 1200px; }

  /* neck label */
  .neck-label { position: absolute; left: 421px; top: 50px; width: 220px; height: 140px; }
  .neck-label svg { position: absolute; inset: 0; }
  .neck-name { position: absolute; top: 28px; width: 100%; text-align: center;
    font-family: "Almendra SC", serif; font-size: 27px; color: var(--neck-text); }
  .neck-sub { position: absolute; top: 64px; width: 100%; text-align: center;
    font-family: "Yellowtail", cursive; font-size: 19px; color: var(--neck-text); }

  /* body labels */
  .label { position: absolute; top: 250px; width: 460px; height: 728px;
    background: var(--paper); border: 7px solid var(--band); overflow: hidden; color: var(--ink); }
  .label.front { left: 41px; }
  .label.back { left: 561px; }
  .torn-band { position: absolute; left: 0; bottom: 0; width: 100%; height: 66px; }

  .header-row { position: absolute; left: 28px; right: 28px; display: flex; justify-content: space-between; align-items: flex-end; }
  .header-word { font-family: "Almendra SC", serif; font-size: 27px; color: var(--ink);
    border-bottom: 1px solid var(--ink-soft); padding-bottom: 6px; }
  .palm { background: radial-gradient(ellipse at 50% 45%, var(--palm) 0%, rgba(138,134,118,0.45) 42%, rgba(231,224,199,0) 70%); }

  .front .header-row { top: 48px; }
  .front .palm { position: absolute; left: 175px; top: 36px; width: 110px; height: 118px; }
  .title { font-family: "Almendra SC", serif; font-weight: 400; color: var(--ink); text-align: center; }
  .front .title { position: absolute; top: 196px; width: 100%; font-size: 56px; letter-spacing: 1px; }
  .script-sub { font-family: "Yellowtail", cursive; font-weight: 400; color: var(--ink); text-align: center; }
  .front .script-sub { position: absolute; top: 272px; width: 100%; font-size: 34px; }
  .short-rule { position: absolute; top: 338px; left: 185px; width: 90px; border-top: 2px solid var(--ink); }
  .names-list { position: absolute; top: 360px; left: 30px; right: 30px; text-align: center;
    font-family: "La Belle Aurore", cursive; font-size: 16.5px; line-height: 25px; color: var(--ink-soft); }

  .spec-row { display: flex; align-items: baseline; font-family: "Libre Baskerville", serif; font-size: 15px; color: var(--ink-soft); }
  .spec-row .liqueur { font-family: "Yellowtail", cursive; font-size: 30px; color: var(--ink); }
  .front .spec-row { position: absolute; top: 600px; left: 130px; right: 36px; justify-content: space-between; }
  .maker-name { position: absolute; font-family: "Almendra SC", serif; font-size: 12px; color: var(--ink-faint); white-space: nowrap; }
  .front .maker-name { left: 22px; top: 614px; }

  .back .title { position: absolute; top: 42px; width: 100%; font-size: 36px; }
  .back .script-sub { position: absolute; top: 84px; width: 100%; font-size: 22px; }
  .back .header-row { top: 124px; left: 12px; right: 12px; }
  .bilingual { position: absolute; top: 196px; left: 10px; right: 10px; height: 410px; }
  .copy { position: absolute; top: 0; width: 168px; font-family: "Courier Prime", monospace; font-size: 12.5px; line-height: 18.5px; color: var(--ink); }
  .copy.fr { left: 0; text-align: left; }
  .copy.en { right: 0; text-align: right; }
  .back .palm { position: absolute; left: 150px; top: 40px; width: 126px; height: 320px; }
  .back .spec-row { position: absolute; top: 604px; left: 0; width: 100%; justify-content: center; }
  .back .maker-name { left: 300px; top: 622px; }
</style>
</head>
<body>
<div class="canvas">

  <div class="neck-label">
    <svg viewBox="0 0 220 140" width="220" height="140">
      <path d="M0 0 H220 V108 H126 L110 136 L94 108 H0 Z" fill="var(--band)"/>
    </svg>
    <div class="neck-name">Voile Cendré</div>
    <div class="neck-sub">Sodabi rectifié</div>
  </div>

  <section class="label front">
    <div class="header-row">
      <span class="header-word">L'Original</span>
      <span class="header-word">Original</span>
    </div>
    <div class="palm" role="img" aria-label="Gravure d'un palmier à huile"></div>
    <h1 class="title">Voile Cendré</h1>
    <p class="script-sub">Sodabi rectifié</p>
    <div class="short-rule"></div>
    <p class="names-list">
      ubusulu · sodabi · tuba · bangui · apéví mimbo ·
      matango · mbuh · kangoya · panam cullee ·
      malafu ya ngasi · lunguila · malafu ya ngasi ·
      bandji · toutou, malamba · doka · nsafufuo ·
      palm wine · yabra Arrak · kallu · tadi · toddy
      · tari · kallu nira · bahar · goribon · tuba ·
      lihan yay ogogoro · segero · tuak · lambanog ·
      bahal bunuk · Seung · poyo · tuak · tua sabu
      legmi mayeet · toddy · vin doux · Dzota
      Concouvi · ezo · Agbéqué · deux doigts akpételé
    </p>
    <span class="maker-name">Voile Cendré</span>
    <div class="spec-row">
      <span>1l</span><span>—</span><span class="liqueur">Liqueur</span><span>—</span><span>43° Vol</span>
    </div>
    <svg class="torn-band" viewBox="0 0 460 66" preserveAspectRatio="none">
      <path d="M0 40 L22 36 L40 40 L58 30 L80 34 L104 22 L126 30 L150 26 L170 34 L196 30 L220 38 L246 34 L268 40 L292 30 L316 36 L340 26 L362 22 L386 30 L408 24 L432 18 L460 22 V66 H0 Z" fill="var(--band)"/>
    </svg>
  </section>

  <section class="label back">
    <h2 class="title">Voile Cendré</h2>
    <p class="script-sub">Sodabi rectifié</p>
    <div class="header-row">
      <span class="header-word">L'Original</span>
      <span class="header-word">Original</span>
    </div>
    <div class="bilingual">
      <div class="palm" role="img" aria-label="Gravure d'un palmier à huile"></div>
      <p class="copy fr">Le Sodabi constitue un reflet d'une culture, un patrimoine. Le produit garde ses valeurs d'origine, de convivialité et d'authenticité. Le Voile Cendré répond à un besoin d'élaboration de nouveaux produits à base du Sodabi artisanal; il allie avec savoir-faire, tradition et tendance pour offrir aux adeptes de ce spiritueux de meilleurs moments de convivialité.</p>
      <p class="copy en">Sodabi is a reflection of a culture, a heritage. The product retains its original values, friendliness and authenticity. Le Voile Cendré responds to a need for the development of new products based on artisanal Sodabi; it combines know-how, tradition and trend to offer fans of this spirit better moments of conviviality.</p>
    </div>
    <div class="spec-row"><span class="liqueur">Liqueur</span></div>
    <span class="maker-name">Voile Cendré</span>
    <svg class="torn-band" viewBox="0 0 460 66" preserveAspectRatio="none">
      <path d="M0 40 L22 36 L40 40 L58 30 L80 34 L104 22 L126 30 L150 26 L170 34 L196 30 L220 38 L246 34 L268 40 L292 30 L316 36 L340 26 L362 22 L386 30 L408 24 L432 18 L460 22 V66 H0 Z" fill="var(--band)"/>
    </svg>
  </section>

</div>
</body>
</html>
```